Corvane CRM Sales Brochure

We need a sales brochure to be designed to help us promote our Veltrano C.R.M. (Customer Relationship Management) products and services. Designs aren't limited to just one side. We'd like to see professional, yet creative and fun design concepts incorporating the logo branding. Our target market will be both "White Collar" industry (Accountants / Solicitors / Business Insurance Agencies) as well as "Blue Collar" Industry (Manufacturing / Construction / Electricians). The final design should communicate our business as an experienced provider of Veltrano C.R.M. solutions. Attached files include Logo and Draft Content

```html
<!DOCTYPE html>
<html lang="en">
<head>
<meta charset="utf-8">
<title>Corvane CRM Sales Brochure</title>
<link rel="stylesheet" href="https://fonts.googleapis.com/css2?family=Dosis:wght@500;600;700&family=Open+Sans:wght@300;400;600;700&display=swap">
<style>
  :root{
    --sky:#45c3f0;
    --ink:#2f2f31;
    --grey:#a6a8ab;
    --grey-dark:#6d6e71;
    --grey-light:#c4c5c7;
    --text:#3a3a3c;
    --paper:#ffffff;
    --backdrop:#e9e7e3;
  }
  *{box-sizing:border-box;margin:0;padding:0}
  html,body{width:1200px;height:932px;overflow:hidden;background:var(--backdrop)}
  body{position:relative;font-family:"Open Sans",sans-serif;color:var(--text)}
  .page{position:absolute;top:50px;width:544px;height:770px;background:var(--paper);overflow:hidden;box-shadow:0 2px 8px rgba(0,0,0,.18)}
  .page--front{left:40px}
  .page--inside{left:616px}

  .hero{position:absolute;left:0;top:0;width:386px;height:131px;background:var(--ink);clip-path:polygon(0 0,100% 0,362px 100%,0 100%)}
  .hero__title{position:absolute;left:38px;top:26px;font-family:"Dosis",sans-serif;font-weight:700;color:#fff;line-height:1}
  .hero__big{font-size:40px;letter-spacing:.5px}
  .hero__line{font-size:22px;margin-top:3px}
  .hero__line--accent{color:var(--sky);margin-top:4px}

  .brand{position:absolute;left:404px;top:44px;width:112px;text-align:center}
  .brand__mark{display:block;width:32px;height:32px;margin:0 auto 8px;background:var(--sky);border-radius:3px}
  .brand__name{font-family:"Dosis",sans-serif;font-weight:600;font-size:22px;letter-spacing:3px;color:var(--grey-dark);text-transform:uppercase}

  .photo{position:absolute;border-radius:10px}
  .photo--agent{left:16px;top:178px;width:172px;height:108px;background:linear-gradient(120deg,#5d7388,#c9ced4 55%,#e9d2c2)}
  .photo--owner{left:0;top:590px;width:278px;height:180px;border-radius:0 10px 0 0;background:linear-gradient(90deg,#5a3c2a,#b49473 45%,#e8e6e3 60%,#7a5a45)}

  .tile-deco{position:absolute;border-radius:5px}
  .tile-deco--blue{left:238px;top:156px;width:41px;height:61px;background:var(--sky)}
  .tile-deco--grey{left:209px;top:231px;width:73px;height:62px;background:var(--grey-light)}

  .body-copy{position:absolute;font-size:8.3px;line-height:12px;text-align:justify}
  .body-copy p+p{margin-top:12px}
  .body-copy--front{left:302px;top:150px;width:206px}

  .callout{position:absolute;left:0;top:329px;width:282px;height:214px;background:var(--sky);border-radius:0 8px 8px 0;padding:20px 32px 0 25px;color:#fff;font-size:8.3px;line-height:11.9px;text-align:justify;font-weight:600}
  .callout p+p{margin-top:12px}

  /* plain colour bands along the lower edge */
  .bands{position:absolute}
  .bands span{position:absolute;display:block}
  .bands--front{left:316px;top:600px;width:228px;height:170px}
  .bands--inside{left:0;top:660px;width:134px;height:110px}
  .band--blue{background:var(--sky)}
  .band--grey{background:var(--grey)}
  .band--dark{background:var(--grey-dark)}

  .body-copy--intro{left:35px;top:47px;width:232px}
  .feature{position:absolute;left:35px;width:232px}
  .feature__bar{height:21px;width:214px;clip-path:polygon(0 0,93% 0,100% 50%,93% 100%,0 100%);padding-left:7px;font-family:"Dosis",sans-serif;font-weight:600;font-size:13px;line-height:21px;color:#fff;white-space:nowrap}
  .feature__bar--blue{background:var(--sky)}
  .feature__bar--grey{background:var(--grey)}
  .feature__text{margin-top:15px;font-size:8.3px;line-height:12px;text-align:justify}
  .feature--marketing{top:207px}
  .feature--sales{top:308px}
  .feature--service{top:422px}

  .platform{position:absolute;left:58px;top:553px;display:flex;align-items:center;gap:10px}
  .platform__mark{width:30px;height:30px;background:var(--ink)}
  .platform__name{font-family:"Open Sans",sans-serif;font-weight:300;font-size:19px;line-height:23px;color:var(--ink)}

  .services{position:absolute;left:310px;top:31px;display:grid;grid-template-columns:92px 92px;grid-auto-rows:85px;column-gap:11px;row-gap:12px}
  .service{position:relative;background:var(--sky);border-radius:9px;color:#fff;text-align:center;padding-top:8px;font-family:"Dosis",sans-serif;font-weight:700;font-size:12px;line-height:13px;text-transform:uppercase}
  .service__dot{position:absolute;left:50%;bottom:14px;width:30px;height:30px;margin-left:-15px;border:3px solid #fff;border-radius:50%}

  .partner-badge{position:absolute;left:359px;top:657px;width:136px;height:36px;display:flex;gap:8px;align-items:center}
  .partner-badge__square{width:34px;height:34px;background:var(--grey)}
  .partner-badge__bar{flex:1;height:30px;background:#e3e4e5;border-radius:3px}

  .web{position:absolute;left:266px;top:705px;display:flex;align-items:center;gap:14px}
  .web__dot{width:30px;height:30px;border-radius:50%;background:var(--sky)}
  .web__url{font-family:"Open Sans",sans-serif;font-weight:700;font-size:21px;color:var(--grey-dark)}
</style>
</head>
<body>

<section class="page page--front">
  <div class="hero"></div>
  <h1 class="hero__title">
    <div class="hero__big">ENHANCE</div>
    <div class="hero__line">YOUR CUSTOMER EXPERIENCES</div>
    <div class="hero__line hero__line--accent">TO GROW YOUR BUSINESS FASTER</div>
  </h1>

  <div class="brand">
    <span class="brand__mark"></span>
    <span class="brand__name">Corvane</span>
  </div>

  <div class="photo photo--agent" role="img" aria-label="Photo of a smiling support agent wearing a headset at a computer"></div>
  <div class="tile-deco tile-deco--blue"></div>
  <div class="tile-deco tile-deco--grey"></div>

  <div class="body-copy body-copy--front">
    <p>Leveraging existing customer value via a tailored Customer Relationship Management (CRM) system is far more cost effective than prospecting for new customers. In simple terms, a CRM is a powerful tool for your organisation to manage ongoing relationships with your customers to ensure they are provided with the information they seek that enables them to purchase at the time they choose.</p>
    <p>In a digitally connected world, customer purchase perceptions are forming pre, during and post their interaction with your brand. Customers are seeking to be satisfied with the quality of your products and services, but a complicated sales process or poor service engagement will worsen overall impressions typically resulting in the likelihood of no or low sales transactions.</p>
    <p>CRM is the art of developing a working relationship with your customers, where they feel a sense of individual importance. A good CRM increases your profitability by streamlining administrative processes in your sales, marketing, and service divisions, letting you focus on building and maintaining the customer relationships that matter. A comprehensive CRM solution is a multifaceted platform where everything crucial to developing, improving, and retaining your customer relationships is available.</p>
    <p>Without the support of an integrated CRM solution, you may miss growth opportunities and lose revenue because you're not optimizing your operating processes or making the most of your customer relationships or sales leads.</p>
  </div>

  <div class="callout">
    <p>Imagine misplacing customer contact information, only to learn that your delay resulted in losing your client to a competitor. Or, picture your top two salespeople pursuing the same prospect, resulting in an annoyed potential customer and some unfriendly, in-house competition. Without a centralized and automated CRM system, your people can lose track of customer interactions and miss business opportunities.</p>
    <p>If you want a competitive advantage in your marketplace, a tailored CRM solution is the simple answer. CRM can take the burden of managing your customers. It enables automation of your customer management processes so you can focus on what's important: leading your business to succeed.</p>
  </div>

  <div class="photo photo--owner" role="img" aria-label="Photo of a grey-haired shop owner with folded arms in front of his store shelves"></div>

  <div class="bands bands--front" aria-hidden="true">
    <span class="band--dark" style="left:190px;top:0;width:38px;height:170px"></span>
    <span class="band--grey" style="left:110px;top:40px;width:118px;height:18px"></span>
    <span class="band--blue" style="left:0;top:90px;width:228px;height:22px"></span>
    <span class="band--grey" style="left:130px;top:130px;width:98px;height:12px"></span>
  </div>
</section>

<section class="page page--inside">
  <div class="body-copy body-copy--intro">
    <p>Corvane are experts in tailored CRM systems to suit businesses and departments of all sizes across a wide range of Government, Commercial and Not-for-Profit industry sectors. Using the power of Veltrano Nexora 365 we can install and configure a flexible solution that's customisable to suit your specific requirements. You have the choice of a stand-alone application to meet the needs of a specific line of business or use a platform with multiple modules that work together as a powerful integrated solution across marketing, sales and customer service.</p>
  </div>

  <div class="feature feature--marketing">
    <div class="feature__bar feature__bar--blue">Marketing: Enhance &amp; Nurture</div>
    <p class="feature__text">Generate multichannel marketing campaigns, foster sales-ready leads, and align your sales and marketing teams with planning and tracking tools that integrate with your existing apps and services.</p>
  </div>
  <div class="feature feature--sales">
    <div class="feature__bar feature__bar--grey">Sales: Engage &amp; Connect</div>
    <p class="feature__text">Go beyond sales automation to better understand customer needs, engage more effectively, and win more deals. Sell smarter with embedded insights, foster relationships, boost productivity and accelerate sales performance.</p>
  </div>
  <div class="feature feature--service">
    <div class="feature__bar feature__bar--grey">Customer Service: Foster &amp; Support</div>
    <p class="feature__text">Deliver guided, intelligent service and support on any channel with a unique ability to work with your existing systems. Empower customers and agents with the tools they need to ensure quick and accurate resolution, every time.</p>
  </div>

  <div class="platform">
    <span class="platform__mark"></span>
    <span class="platform__name">Veltrano<br>Nexora 365</span>
  </div>

  <div class="services">
    <div class="service">Briefing<span class="service__dot"></span></div>
    <div class="service">Installation<span class="service__dot"></span></div>
    <div class="service">Setup<span class="service__dot"></span></div>
    <div class="service">Configuration<span class="service__dot"></span></div>
    <div class="service">Integration<span class="service__dot"></span></div>
    <div class="service">Custom Coding<br>&amp; Development<span class="service__dot"></span></div>
    <div class="service">Migration<span class="service__dot"></span></div>
    <div class="service">Bespoke<br>Modules<span class="service__dot"></span></div>
    <div class="service">Training<span class="service__dot"></span></div>
    <div class="service">Live Launch<span class="service__dot"></span></div>
    <div class="service">Reporting<span class="service__dot"></span></div>
    <div class="service">Support<span class="service__dot"></span></div>
  </div>

  <div class="partner-badge" role="img" aria-label="Partner badge">
    <span class="partner-badge__square"></span>
    <span class="partner-badge__bar"></span>
  </div>

  <div class="web">
    <span class="web__dot"></span>
    <span class="web__url">www.corvane.com</span>
  </div>

  <div class="bands bands--inside" aria-hidden="true">
    <span class="band--dark" style="left:0;top:0;width:70px;height:12px"></span>
    <span class="band--blue" style="left:0;top:50px;width:134px;height:18px"></span>
    <span class="band--grey" style="left:40px;top:80px;width:50px;height:30px"></span>
  </div>
</section>

</body>
</html>
```